Certificate of Completion - Educational Trainings

We are looking for a certificate of completion for individuals who complete one of our specific trainings. Files should be provided in a Word (docx) or PowerPoint (pptx) format. The "Talmoray example.png" file is to show necessary information. Copies of logos have been included for design purposes.

Target Market(s)

Training Participants

Industry/Entity Type

Healthcare

Font styles to use
Sans Serif

```html
<!DOCTYPE html>
<html lang="en">
<head>
<meta charset="UTF-8">
<title>Talmoray Certificate of Completion</title>
<link rel="stylesheet" href="https://fonts.googleapis.com/css2?family=Cormorant+Garamond:wght@500;700&family=Josefin+Sans:wght@400&family=Montserrat:wght@700&family=Poppins:wght@400&family=Source+Sans+3:wght@400&display=swap">
<style>
  :root {
    --green: #3f8a26;
    --green-deep: #256b0a;
    --green-tint: #eef5ea;
    --teal: #0c5656;
    --ink: #111111;
    --text: #3b3b4f;
    --frame: #555555;
    --paper: #ffffff;
  }
  html, body { margin: 0; padding: 0; overflow: hidden; background: var(--paper); }
  .certificate {
    position: relative;
    width: 1200px;
    height: 849px;
    overflow: hidden;
    background: var(--green-tint);
  }
  .edge-band {
    position: absolute;
    left: 0; width: 1200px; height: 16px;
    background: var(--green-deep);
  }
  .edge-band-top { top: 0; }
  .edge-band-bottom { bottom: 0; }
  .panel {
    position: absolute;
    left: 86px; top: 87px;
    width: 1025px; height: 675px;
    box-sizing: border-box;
    background: var(--paper);
    border: 3px solid var(--frame);
    border-radius: 18px;
  }
  .panel-inner {
    position: absolute;
    left: 100px; top: 101px;
    width: 997px; height: 647px;
    box-sizing: border-box;
    border: 1px solid var(--green);
    border-radius: 10px;
  }
  .line-text {
    position: absolute;
    left: 600px;
    transform: translateX(-50%);
    white-space: nowrap;
    margin: 0;
    text-align: center;
  }
  .brand {
    top: 132px;
    display: flex;
    align-items: center;
    gap: 8px;
    font-family: "Montserrat", sans-serif;
    font-weight: 700;
    font-size: 21px;
    letter-spacing: 1.5px;
    color: var(--ink);
  }
  .brand-dot { width: 16px; height: 16px; border-radius: 50%; background: var(--green-deep); }
  .address {
    top: 174px;
    font-family: "Josefin Sans", sans-serif;
    font-size: 23px;
    color: var(--ink);
  }
  .registry {
    top: 205px;
    font-family: "Cormorant Garamond", serif;
    font-weight: 500;
    font-size: 25px;
    letter-spacing: 0.5px;
    color: var(--ink);
  }
  .title {
    top: 245px;
    font-family: "Cormorant Garamond", serif;
    font-weight: 700;
    font-size: 49px;
    letter-spacing: 2px;
    color: var(--teal);
  }
  .awarded {
    top: 312px;
    font-family: "Source Sans 3", sans-serif;
    font-size: 21px;
    color: var(--text);
  }
  .name-line {
    position: absolute;
    left: 282px; top: 469px;
    width: 657px; height: 0;
    border-top: 1.5px solid var(--ink);
  }
  .course {
    top: 488px;
    font-family: "Source Sans 3", sans-serif;
    font-size: 21px;
    line-height: 31px;
    color: var(--text);
  }
  .signature {
    position: absolute;
    width: 180px;
    text-align: center;
    font-family: "Source Sans 3", sans-serif;
    font-size: 21px;
    color: var(--text);
  }
  .signature::before {
    content: "";
    display: block;
    width: 156px;
    margin: 0 auto 4px;
    border-top: 1px solid var(--frame);
  }
  .signature-date { left: 320px; top: 638px; }
  .signature-consultant { left: 714px; top: 636px; }
  .seal-name {
    top: 646px;
    display: flex;
    align-items: center;
    gap: 8px;
    font-family: "Montserrat", sans-serif;
    font-weight: 700;
    font-size: 24px;
    letter-spacing: 1px;
    color: var(--green-deep);
  }
  .seal-square { width: 16px; height: 16px; background: var(--green-deep); }
  .footnote {
    top: 687px;
    font-family: "Poppins", sans-serif;
    font-size: 13.5px;
    line-height: 16px;
    letter-spacing: 0.4px;
    color: var(--ink);
  }
</style>
</head>
<body>
<main class="certificate">
  <div class="edge-band edge-band-top"></div>
  <div class="edge-band edge-band-bottom"></div>
  <div class="panel"></div>
  <div class="panel-inner"></div>

  <div class="line-text brand"><span class="brand-dot"></span>TALMORAY</div>
  <p class="line-text address">48 HARBOR LANE, STE. 310 BRUNSWICK, ME 04011</p>
  <p class="line-text registry">NATIONAL REGISTRY SPONSOR NUMBER 58217</p>
  <h1 class="line-text title">CERTIFICATE OF COMPLETION</h1>
  <p class="line-text awarded">This certificate is awarded to :</p>
  <div class="name-line"></div>
  <p class="line-text course">For Successful Completion of Best Practices :<br>Budget Process / Budget Building<br>Completed Online Field of Study Finance (CPE Credits: 1)</p>

  <div class="signature signature-date">Completion Date</div>
  <div class="line-text seal-name"><span class="seal-square"></span>Talmoray</div>
  <div class="signature signature-consultant">Senior Consultant</div>

  <p class="line-text footnote">In Accordance with the Standard of The National Board of CPE Sponsors,<br>CPE Credits Have Been Granted Based on A 50 Minute Hour.</p>
</main>
</body>
</html>
```